Vex9Tax Business Card

Need a new business card for my law firm. The major components for the card will be my logo "Vex9Tax," the photo of me, contact information, and a QR Code for my website vex9tax.com. If you are unable to generate a QR Code, let me know and I'll see if I can make one. For the "Vex9Tax" logo, don't worry about the "Ride The Wave" part, you can leave that out. Here are my and the firm details:
Benedicto R Salazar III
Attorney at Law
Address: 250 Harbor Plaza, Suite 400
Dallas, TX 75201
Office #: 877-482-6173
Cell #: 214-657-3381
Fax #: 469-738-5126
Email: vex@vex9tax.com
Website: vex9tax.com

```html
<!DOCTYPE html>
<html lang="en">
<head>
<meta charset="utf-8">
<title>Vex9Tax Business Card</title>
<link rel="stylesheet" href="https://fonts.googleapis.com/css2?family=Ubuntu:wght@400;700&display=swap">
<style>
  :root {
    --page: #ffffff;
    --card-dark: #000000;
    --card-light: #ffffff;
    --ink-light: #ffffff;
    --ink-dark: #111111;
    --accent: #38c6f4;
    --photo-top: #6b6460;
    --photo-bottom: #2a2a30;
  }
  html, body {
    margin: 0;
    padding: 0;
    width: 1200px;
    height: 1200px;
    overflow: hidden;
    background: var(--page);
  }
  .canvas {
    position: relative;
    width: 1200px;
    height: 1200px;
  }
  .card {
    position: absolute;
    left: 166px;
    width: 869px;
    height: 509px;
    box-shadow: 0 2px 8px rgba(0,0,0,0.25);
  }
  .card--front { top: 66px; background: var(--card-dark); }
  .card--back { top: 626px; background: var(--card-light); }

  .portrait-frame {
    position: absolute;
    left: 56px;
    top: 39px;
    width: 215px;
    height: 310px;
  }
  .portrait-frame svg { display: block; }

  .wordmark {
    position: absolute;
    display: block;
  }
  .wordmark text {
    font-family: "Ubuntu", sans-serif;
    font-weight: 700;
  }
  .wordmark--front { left: 438px; top: 40px; }
  .wordmark--back { left: 117px; top: 180px; }

  .contact-list {
    position: absolute;
    right: 52px;
    top: 196px;
    margin: 0;
    padding: 0;
    list-style: none;
    font-family: "Ubuntu", sans-serif;
    font-size: 21px;
    color: var(--ink-light);
  }
  .contact-list li {
    display: flex;
    align-items: center;
    justify-content: flex-end;
    height: 33.7px;
  }
  .contact-list .icon {
    width: 14px;
    height: 14px;
    margin-left: 12px;
    flex: none;
  }
  .address {
    position: absolute;
    right: 52px;
    top: 405px;
    display: flex;
    align-items: flex-start;
    font-family: "Ubuntu", sans-serif;
    font-size: 21px;
    line-height: 28px;
    color: var(--ink-light);
    text-align: right;
    font-style: normal;
  }
  .address .icon {
    width: 14px;
    height: 16px;
    margin-left: 12px;
    margin-top: 5px;
  }
  .attorney {
    position: absolute;
    left: 57px;
    top: 402px;
    font-family: "Ubuntu", sans-serif;
    color: var(--ink-light);
  }
  .attorney-name {
    margin: 0;
    font-size: 28px;
    font-weight: 700;
    line-height: 36px;
  }
  .attorney-title {
    margin: 0;
    font-size: 21px;
    line-height: 26px;
  }
</style>
</head>
<body>
<main class="canvas">

  <section class="card card--front">
    <div class="portrait-frame">
      <svg width="215" height="310" viewBox="0 0 215 310">
        <defs>
          <linearGradient id="portrait-tone" x1="0" y1="0" x2="0" y2="1">
            <stop offset="0" stop-color="#6b6460"/>
            <stop offset="1" stop-color="#2a2a30"/>
          </linearGradient>
        </defs>
        <path class="frame-arch" d="M0 0 H135 A80 80 0 0 1 215 80 V310 H0 Z" fill="#38c6f4"/>
        <path class="portrait" role="img" aria-label="Portrait photo of the attorney" d="M0 310 V114 A90 90 0 0 1 180 114 V245 A65 65 0 0 1 115 310 Z" fill="url(#portrait-tone)"/>
      </svg>
    </div>

    <svg class="wordmark wordmark--front" width="375" height="80" viewBox="0 0 375 80">
      <text x="2" y="63" font-size="58" textLength="370" lengthAdjust="spacing" fill="#ffffff">VEX9TAX</text>
    </svg>

    <ul class="contact-list">
      <li>877-482-6173
        <svg class="icon" viewBox="0 0 16 16"><path d="M3 1l3 3-1.5 2a9 9 0 0 0 5.5 5.5L12 10l3 3-2 2C7 15 1 9 1 3z" fill="#38c6f4"/></svg>
      </li>
      <li>214-657-3381
        <svg class="icon" viewBox="0 0 16 16"><rect x="4" y="1" width="8" height="14" rx="1.5" fill="none" stroke="#38c6f4" stroke-width="2"/><circle cx="8" cy="12" r="1" fill="#38c6f4"/></svg>
      </li>
      <li>469-738-5126
        <svg class="icon" viewBox="0 0 16 16"><rect x="4" y="1" width="8" height="4" fill="#38c6f4"/><rect x="1" y="6" width="14" height="6" rx="1" fill="#38c6f4"/><rect x="4" y="10" width="8" height="5" fill="#38c6f4"/></svg>
      </li>
      <li>vex@vex9tax.com
        <svg class="icon" viewBox="0 0 16 16"><rect x="1" y="3" width="14" height="10" rx="1" fill="#38c6f4"/><path d="M1.5 4l6.5 5 6.5-5" fill="none" stroke="#000000" stroke-width="1.3"/></svg>
      </li>
      <li>vex9tax.com
        <svg class="icon" viewBox="0 0 16 16"><circle cx="8" cy="8" r="6.5" fill="none" stroke="#38c6f4" stroke-width="1.6"/><ellipse cx="8" cy="8" rx="3" ry="6.5" fill="none" stroke="#38c6f4" stroke-width="1.3"/><path d="M1.5 8h13" stroke="#38c6f4" stroke-width="1.3"/></svg>
      </li>
    </ul>

    <address class="address">
      <span>250 Harbor Plaza, Suite 400<br>Dallas, TX 75201</span>
      <svg class="icon" viewBox="0 0 14 16"><path d="M7 0a5.5 5.5 0 0 0-5.5 5.5C1.5 10 7 16 7 16s5.5-6 5.5-10.5A5.5 5.5 0 0 0 7 0z" fill="#38c6f4"/><circle cx="7" cy="5.5" r="2" fill="#000000"/></svg>
    </address>

    <div class="attorney">
      <p class="attorney-name">Benedicto R Salazar III</p>
      <p class="attorney-title">Attorney at Law</p>
    </div>
  </section>

  <section class="card card--back">
    <svg class="wordmark wordmark--back" width="635" height="110" viewBox="0 0 635 110">
      <text x="2" y="100" font-size="94" textLength="630" lengthAdjust="spacing" fill="#111111">VEX9TAX</text>
    </svg>
  </section>

</main>
</body>
</html>
```